VANTAGE Conference Retractable Standing Banner

I need a design for a 32X80 in retractable banner for a conference. The full title of the conference is the OMRA QLDWN Symposium for Studies on Lasting Involvement in Design, Informatics, and Science. The short name of the conference is VANTAGE. The conference is an academic research conference on equity, diversity, and inclusion in computing, attended by faculty researchers from universities across the US. <br/><br/>Our website is at http://vantage2020.qldwn-example.org. <br/><br/>We typically use the colors purple and white, but are open to other colors being integrated into the design. I attached some previous (terrible) logos just so that you can get an idea of what information we've felt it is important to convey and the color scheme. I would prefer to have something more impactful/graphic in a design.<br/><br/>We prefer clean designs with geometric shapes, and with graphic interest.

Target Market(s)

academic researchers, professors, computer scientists, social scientists, those interested in diversity, equity, and inclusion

Logo Text

VANTAGE

Font styles to use
Sans Serif

Colors
6b449b
33a6d7

Requirements
Must have
• The logo must have the short name of the conference, which is VANTAGE
Nice to have
• The full name of the conference is:
• OMRA QLDWN Symposium for Studies on Fairness and Lasting Involvement in Design, Informatics, and Science (VANTAGE)
• It would be nice to work something in that either includes the words "research on equity and inclusion in computing" or some graphic that captures that concept.
Should not have
• Please don't use 1's and 0's to represent computing - we want to dispel that stereotype.

```html
<!DOCTYPE html>
<html lang="en">
<head>
<meta charset="utf-8">
<title>VANTAGE Conference Retractable Banner</title>
<link href="https://fonts.googleapis.com/css2?family=Montserrat:wght@400;500;600;700;800&display=swap" rel="stylesheet">
<style>
  :root {
    --page: #e8e8eb;
    --white: #ffffff;
    --logo-purple: #4b2c82;
    --ink: #333338;
    --blue: #0b8ff3;
    --blue-light: #2aa3ff;
    --navy: #15195a;
    --purple: #46108a;
    --purple-deep: #3a1596;
  }
  * { margin: 0; padding: 0; box-sizing: border-box; }
  html, body {
    width: 1200px;
    height: 2397px;
    overflow: hidden;
    background: var(--page);
    font-family: "Montserrat", Arial, sans-serif;
  }
  .banner {
    position: absolute;
    left: 160px;
    top: 24px;
    width: 880px;
    height: 2349px;
    overflow: hidden;
    box-shadow: 0 10px 30px rgba(0,0,0,0.18);
  }
  .banner-shapes {
    position: absolute;
    inset: 0;
    width: 100%;
    height: 100%;
  }
  .logo {
    position: absolute;
    left: 92px;
    top: 150px;
    display: flex;
    align-items: center;
    gap: 22px;
  }
  .logo-name {
    font-size: 116px;
    font-weight: 600;
    letter-spacing: 1px;
    line-height: 1;
    color: var(--logo-purple);
  }
  .logo-dot {
    width: 40px;
    height: 40px;
    border-radius: 50%;
    background: var(--logo-purple);
    margin-top: -60px;
  }
  .divider {
    position: absolute;
    height: 6px;
    background: var(--ink);
  }
  .divider.top { left: 393px; top: 313px; width: 96px; }
  .divider.bottom { left: 407px; top: 2007px; width: 66px; background: var(--white); }
  .event-title {
    position: absolute;
    left: 100px;
    top: 338px;
    font-size: 54px;
    line-height: 1.2;
    color: var(--ink);
    font-weight: 500;
    white-space: nowrap;
  }
  .event-title .org { color: var(--blue); font-weight: 700; }
  .event-subtitle {
    position: absolute;
    left: 102px;
    top: 410px;
    font-size: 28px;
    line-height: 38px;
    font-weight: 500;
    color: var(--ink);
  }
  .event-date {
    position: absolute;
    left: 102px;
    top: 510px;
    width: 406px;
    height: 74px;
    background: var(--blue);
    color: var(--white);
    font-size: 27px;
    font-weight: 700;
    display: flex;
    align-items: center;
    padding-left: 20px;
  }
  .tagline {
    position: absolute;
    left: 0;
    width: 100%;
    text-align: center;
    color: var(--white);
  }
  .tagline-head {
    top: 1680px;
    font-size: 104px;
    font-weight: 800;
    letter-spacing: 1px;
  }
  .tagline-sub {
    top: 1826px;
    font-size: 52px;
    line-height: 64px;
    font-weight: 400;
  }
  .website {
    position: absolute;
    left: 121px;
    top: 2066px;
    width: 640px;
    height: 85px;
    border-radius: 6px;
    background: linear-gradient(180deg, var(--blue-light), var(--blue));
    color: var(--white);
    font-size: 30px;
    font-weight: 400;
    display: flex;
    align-items: center;
    justify-content: center;
    white-space: nowrap;
  }
  .website b { font-weight: 700; }
</style>
</head>
<body>
  <div class="banner">
    <svg class="banner-shapes" viewBox="0 0 414 1105" preserveAspectRatio="none" aria-hidden="false">
      <defs>
        <radialGradient id="photoGlow" cx="0.62" cy="0.45" r="0.6">
          <stop offset="0" stop-color="#2c8cf0"/>
          <stop offset="0.35" stop-color="#1a49b8"/>
          <stop offset="1" stop-color="#131852"/>
        </radialGradient>
        <linearGradient id="purpleField" x1="0" y1="0" x2="0" y2="1">
          <stop offset="0" stop-color="#4a0d86"/>
          <stop offset="0.6" stop-color="#42128e"/>
          <stop offset="1" stop-color="#3a1a9c"/>
        </linearGradient>
      </defs>
      <rect class="field-white" x="0" y="0" width="414" height="1105" fill="#ffffff"/>
      <polygon class="field-photo" role="img" aria-label="Photo of an open hand holding a glowing network sphere of technology icons above a blue planet" points="0,498 414,225 414,782 0,506" fill="url(#photoGlow)"/>
      <polygon class="accent-triangle" points="0,260 172,367 0,487" fill="#0b8ff3"/>
      <polygon class="field-purple" role="img" aria-label="Purple field with faint network lines" points="0,517 414,795 414,1105 0,1105" fill="url(#purpleField)"/>
    </svg>

    <div class="logo">
      <span class="logo-name">VANTAGE</span>
      <span class="logo-dot"></span>
    </div>
    <div class="divider top"></div>
    <div class="event-title"><span class="org">OMRA QLDWN</span> Symposium</div>
    <div class="event-subtitle">for Studies on Lasting Involvement<br>in Design, Informatics, and Science.</div>
    <div class="event-date">March 11, 2020 | Portland,</div>

    <div class="tagline tagline-head">RESEARCH</div>
    <div class="tagline tagline-sub">On Equity and Inclusion<br>In Computing</div>
    <div class="divider bottom"></div>
    <div class="website">www.<b>vantage2020</b>.qldwn-example.org</div>
  </div>
</body>
</html>
```